New look modernised front page for Pellmark Sporting League Website Which incorporates our new logo (to be provided as a png file)
We want the home page to a panel to allow an image rotator and provide ready access to links to other inflation via some link menus/panel/button
1. Join a Croquet Club - links to details about Croquet in NSW - gateway to information of interest or the general public/“interested others” eg about the game, clubs locations and contacts
2. Club and Member Information - newsletters, Calender of events, and downloads
3. Officials and volunteers - training resources etc
4. Member and Club sign in - access to database
5. About Us - information about Pellmark Sporting League incorporated -peak body for croquet in NSW - governance, contact details etc

Current website is at https://www.pellmark-league.org/index.html

Target Market(s)

Dual target - People interested in learning about croquet and existing members

Number of Pages Required

1 page

Font styles to use
Sans Serif

Colors
0255a3
3377b5
85acd3
85cae6
33a6d7
0792cd
00a990

Requirements
Must have
• Contemporary feel
• Include logo - file attached
• Colours to include blues which are the NSW colour
Nice to have
• We want the home page to a panel to allow an image rotator and provide ready access to links to other inflation via some link menus/panel/button
• 1. Join a Croquet Club - links to details about Croquet in NSW - gateway to information of interest or the general public/“interested others” eg about the game, clubs locations and contacts
• 2. Club and Member Information - newsletters, Calender of events, and downloads
• 3. Officials and volunteers - training resources etc
• 4. Member and Club sign in - access to database
• 5. About Us - information about Pellmark Sporting League incorporated -peak body for croquet in NSW - governance, contact details etc
• Want to have feeling of activity/movement/alive
• Current website is at https://www.pellmark-league.org/index.html
• Some photos attached for information

```html
<!DOCTYPE html>
<html lang="en">
<head>
<meta charset="utf-8">
<title>Pellmark Sporting League</title>
<link rel="stylesheet" href="https://fonts.googleapis.com/css2?family=Montserrat:wght@400;500;600;700&display=swap">
<style>
:root{
  --navy:#0255a3;
  --blue:#3377b5;
  --sky:#85acd3;
  --teal:#00a990;
  --text:#333;
  --muted:#555;
  --light:#f7f7f7;
  --card-border:#eceff3;
  --footer:#2b2b2b;
  --footer-line:#444;
  --white:#fff;
}
*{box-sizing:border-box;margin:0;padding:0}
html,body{width:1200px;height:3061px;overflow:hidden}
body{font-family:"Montserrat",Arial,sans-serif;color:var(--text);background:var(--white);position:relative}
a{color:var(--blue);text-decoration:none}
.container{position:relative;width:902px;margin:0 auto;height:100%}
.abs{position:absolute}

/* header */
.site-header{height:60px;position:relative}
.brand{position:absolute;left:149px;top:17px;font-size:20px;font-weight:600;color:var(--navy)}
.main-nav{position:absolute;left:428px;top:22px;display:flex;gap:28px;font-size:12px;font-weight:600;letter-spacing:.5px}
.main-nav a{color:#222}
.main-nav a.active{color:var(--sky)}
.main-nav a.current{color:var(--navy)}
.btn{display:inline-flex;align-items:center;justify-content:center;border-radius:20px;font-size:12px;font-weight:700;letter-spacing:.6px;text-transform:uppercase}
.btn-signup{position:absolute;left:941px;top:13px;width:106px;height:34px;background:var(--teal);color:var(--white)}

/* hero */
.hero{position:relative;height:375px;overflow:hidden}
.hero-photo{position:absolute;inset:0;background:linear-gradient(180deg,#4d5a48 0%,#2f3d2c 45%,#24331f 100%)}
.hero-shade{position:absolute;inset:0;background:rgba(0,0,0,.35)}
.hero h1{position:absolute;top:110px;width:100%;text-align:center;color:var(--white);font-size:33px;font-weight:600}
.hero p{position:absolute;top:170px;width:100%;text-align:center;color:var(--white);font-size:14px;font-weight:600}
.hero-actions{position:absolute;top:218px;left:0;width:100%;display:flex;justify-content:center;gap:16px}
.hero-actions .btn{width:150px;height:38px;font-size:11px}
.btn-teal{background:var(--teal);color:var(--white)}
.btn-white{background:var(--white);color:#222}
.hero-arrow{position:absolute;top:171px;width:30px;height:30px;border-radius:50%;background:var(--navy);display:flex;align-items:center;justify-content:center}
.hero-dots{position:absolute;top:310px;left:0;width:100%;display:flex;justify-content:center;gap:12px}
.hero-dots span{width:11px;height:11px;border-radius:50%;background:var(--white)}
.hero-dots span.on{background:var(--navy)}

/* section titles */
.section-title{position:absolute;top:0;width:100%;text-align:center;font-size:27px;font-weight:500;color:var(--navy);letter-spacing:.5px}
.sub-title{display:flex;align-items:center;gap:8px;font-size:20px;font-weight:600;color:var(--teal)}
.sub-title::before{content:"";width:12px;height:12px;border:2.5px solid var(--teal);border-radius:50%}
.body-text{font-size:12.5px;line-height:1.5;color:var(--muted)}
.read-more{font-size:11.5px;font-weight:700;color:var(--navy);letter-spacing:.5px;text-transform:uppercase}

/* about */
.about{height:535px;position:relative;padding-top:38px}
.about .container{height:497px}
.about-col{position:absolute;left:0;width:352px}
.about-photo{position:absolute;left:406px;top:61px;width:496px;height:355px;background:linear-gradient(180deg,#8fa07c 0%,#6c7d55 50%,#55653e 100%);box-shadow:0 3px 10px rgba(0,0,0,.2)}

/* join club */
.join{height:560px;background:var(--light);padding-top:50px}
.join .container{height:510px}
.feature-cards{position:absolute;top:79px;left:0;display:flex;gap:11px}
.feature-card{width:294px;height:375px;background:var(--white);box-shadow:0 1px 4px rgba(0,0,0,.06);padding:150px 17px 0;position:relative;text-align:left}
.feature-icon{position:absolute;top:38px;left:87px;width:120px;height:120px}
.feature-card h3{text-align:center;font-size:14px;font-weight:600;color:var(--teal);margin:26px 0 12px;letter-spacing:.4px}
.feature-card .body-text{font-size:12.5px}
.feature-card a{display:block;font-size:12.5px;line-height:1.5}

/* news */
.news{height:555px;padding-top:46px}
.news .container{height:509px}
.tabs{position:absolute;top:81px;left:0;display:flex;gap:16px}
.tab{width:151px;height:44px;display:flex;align-items:center;justify-content:center;font-size:11px;font-weight:600;letter-spacing:.5px;background:#f2f2f2;color:#333}
.tab.active{background:var(--teal);color:var(--white)}
.news-cards{position:absolute;top:250px;left:0;display:flex;gap:11px}
.news-card{width:294px;height:200px;border:1px solid var(--card-border);box-shadow:0 1px 4px rgba(0,0,0,.05);padding:14px 38px 0}
.news-card h4{text-align:center;font-size:14px;font-weight:600;color:var(--navy);margin-bottom:8px;letter-spacing:.4px}
.news-card ul{list-style:none}
.news-card li{font-size:12.5px;line-height:1.5;color:var(--muted);position:relative;margin-bottom:6px}
.news-card li::before{content:"";position:absolute;left:-17px;top:7px;width:6px;height:6px;border-radius:50%;background:#bbb}
.news-card .read-more{display:block;margin-top:10px}

/* officials */
.officials{height:603px;background:var(--light);padding-top:45px}
.officials .container{height:558px}
.gallery{position:absolute;top:63px;left:153px;display:grid;grid-template-columns:294px 293px;grid-template-rows:210px 214px;gap:10px 8px}
.tile{position:relative}
.tile-play{background:linear-gradient(180deg,#8aa083 0%,#8fae6a 60%,#7b9b57 100%)}
.tile-support{background:linear-gradient(180deg,#2a66ae,#1d57a0);color:var(--white);text-align:center;padding:52px 40px 0}
.tile-support h5{font-size:14px;font-weight:600;letter-spacing:.5px;margin-bottom:12px}
.tile-support p{font-size:12px;line-height:1.6}
.tile-gear{background:linear-gradient(180deg,#b8b6ae 0%,#a29f94 100%)}
.tile-night{background:linear-gradient(180deg,#1a1a1e 0%,#2e2a28 60%,#5a4d40 100%)}

/* footer */
.site-footer{height:373px;background:var(--footer);color:var(--white);position:relative}
.footer-col{position:absolute;top:46px}
.footer-col h6{font-size:20px;font-weight:500;color:var(--teal);letter-spacing:1px;margin-bottom:20px}
.footer-label{font-size:13px;font-weight:700;margin:0 0 3px}
.footer-text{font-size:13px;line-height:1.7}
.footer-links{list-style:none;text-align:center;font-size:13px;line-height:22.5px}
.footer-links a{color:var(--white)}
.subscribe{display:flex;margin-top:16px}
.subscribe input{width:232px;height:38px;border:0;background:#555;color:#ddd;font-family:inherit;font-size:11px;font-weight:600;letter-spacing:.6px;padding-left:22px}
.subscribe button{width:68px;height:38px;border:0;background:var(--teal);color:var(--white);font-family:inherit;font-size:11px;font-weight:700;letter-spacing:.6px}
.social{display:flex;gap:9px;margin-top:14px}
.social span{width:44px;height:44px;border-radius:50%;background:#5a5a5a;display:flex;align-items:center;justify-content:center}
.copyright{position:absolute;left:0;bottom:0;width:100%;height:70px;border-top:1px solid var(--footer-line);display:flex;align-items:center;justify-content:center;font-size:14px;font-weight:600}
</style>
</head>
<body>

<header class="site-header">
  <div class="brand">Pellmark Sporting League</div>
  <nav class="main-nav">
    <a class="active" href="#">HOME</a>
    <a href="#">ABOUT US</a>
    <a class="current" href="#">CLUBS</a>
    <a href="#">OFFICIALS</a>
    <a href="#">EVENTS</a>
    <a href="#">CONTACT</a>
  </nav>
  <a class="btn btn-signup" href="#">Sign up</a>
</header>

<section class="hero">
  <div class="hero-photo" role="img" aria-label="Croquet lawn with coloured balls and a player's mallet"></div>
  <div class="hero-shade"></div>
  <h1>Join Pellmark Sporting League</h1>
  <p>Lorem Ipsum is simply dummy text of the printing and typesetting industry.</p>
  <div class="hero-actions">
    <a class="btn btn-teal" href="#">Join Club</a>
    <a class="btn btn-white" href="#">How to play</a>
  </div>
  <a class="hero-arrow" style="left:165px" href="#" aria-label="Previous slide"><svg width="12" height="12" viewBox="0 0 12 12"><path d="M8 1 3 6l5 5" fill="none" stroke="#fff" stroke-width="1.6"/></svg></a>
  <a class="hero-arrow" style="left:1005px" href="#" aria-label="Next slide"><svg width="12" height="12" viewBox="0 0 12 12"><path d="m4 1 5 5-5 5" fill="none" stroke="#fff" stroke-width="1.6"/></svg></a>
  <div class="hero-dots"><span class="on"></span><span></span><span></span></div>
</section>

<section class="about">
  <div class="container">
    <h2 class="section-title">ABOUT US</h2>
    <div class="about-col" style="top:80px">
      <div class="sub-title">Pellmark League</div>
      <p class="body-text" style="margin:8px 0 6px">Pellmark Sporting League is the State organisation responsible for promoting, organising and developing the sport of Croquet in NSW. It also is charged with maintaining a uniform handicapping system and coordinating croquet activities throughout the state.</p>
      <a class="read-more" href="#">Read more</a>
    </div>
    <div class="about-col" style="top:246px">
      <div class="sub-title">Governance</div>
      <p class="body-text" style="margin-top:8px"><a href="#">Click here</a> to view profiles of members of the current PSL Board of Directors.</p>
      <p class="body-text" style="margin-top:18px"><a href="#">Click here</a> to view PSL Meeting and other administrative events this year from this month onward.</p>
    </div>
    <div class="about-photo" role="img" aria-label="Group of croquet players in whites standing on a lawn"></div>
  </div>
</section>

<section class="join">
  <div class="container">
    <h2 class="section-title">JOIN CLUB</h2>
    <div class="feature-cards">
      <article class="feature-card">
        <svg class="feature-icon" viewBox="0 0 120 120" fill="none" stroke="#00a990" stroke-width="3"><circle cx="60" cy="60" r="57"/><path d="M42 84V56a8 8 0 0 1 16 0v28M72 42v42M72 48h10v8h-10"/></svg>
        <h3>ABOUT GAME</h3>
        <p class="body-text">Croquet is a very old game that had its beginnings in the early 1400's. Below is a brief history of the game. England developed the initial rules of the game in the mid 1800's.</p>
        <a class="read-more" href="#" style="margin-top:4px">Read more</a>
      </article>
      <article class="feature-card">
        <svg class="feature-icon" viewBox="0 0 120 120" fill="none" stroke="#00a990" stroke-width="3"><circle cx="60" cy="60" r="57"/><path d="M60 86C48 72 42 62 42 52a18 18 0 0 1 36 0c0 10-6 20-18 34Z"/><circle cx="60" cy="52" r="6"/><path d="M46 82c-8 2-12 4-12 6 0 4 12 6 26 6s26-2 26-6c0-2-4-4-12-6"/></svg>
        <h3>CLUB LOCATION</h3>
        <p class="body-text">Clubs maintain information about their office bearers, contact details, playing days, etc and are responsible for it being correct.</p>
        <a href="#">Clubs in sydney</a>
        <a href="#">Clubs in country NSW and ACT</a>
        <a href="#">All clubs in NSW and ACT</a>
      </article>
      <article class="feature-card">
        <svg class="feature-icon" viewBox="0 0 120 120" fill="none" stroke="#00a990" stroke-width="3"><circle cx="60" cy="60" r="57"/><path d="M44 90V30M44 32h36l-8 10 8 10H44"/></svg>
        <h3>REGIONS</h3>
        <p class="body-text">PSL has divided its affiliated clubs into 9 regions, eazch with a coordinator.</p>
        <a href="#">Regions, their Clubs and their Coordinators</a>
        <p class="body-text">Currently this website continues to classify clubs as Sydney (Metropolitan) or Country.</p>
      </article>
    </div>
  </div>
</section>

<section class="news">
  <div class="container">
    <h2 class="section-title">NEWS &amp; EVENTS</h2>
    <div class="tabs">
      <span class="tab active">NEWSLETTER</span>
      <span class="tab">EVENTS</span>
      <span class="tab">DOWNLOADS</span>
    </div>
    <div class="abs" style="top:166px;left:0">
      <div class="sub-title">Recent PSL Newsletters</div>
      <p class="body-text" style="font-size:12px;margin-top:8px">Newsletters are in PDF format which can be viewed using Folio Reader, if this is not installed on your computer <a href="#">click</a> here to download it</p>
    </div>
    <div class="news-cards">
      <article class="news-card">
        <h4>JUNE - 2018</h4>
        <ul><li>Trans Tasman AC Test Series</li><li>A Gong for Mosman</li><li>Jenna Hollis wins the Australian Women's AC Open 2018 Eire Cup, Adelaide</li></ul>
        <a class="read-more" href="#">Read more</a>
      </article>
      <article class="news-card">
        <h4>MARCH - 2018</h4>
        <ul><li>Trans Tasman AC Test Series</li><li>A Gong for Mosman</li><li>Jenna Hollis wins the Australian Women's AC Open 2018 Eire Cup, Adelaide</li></ul>
        <a class="read-more" href="#">Read more</a>
      </article>
      <article class="news-card">
        <h4>DECEMBER - 2018</h4>
        <ul><li>Trans Tasman AC Test Series</li><li>A Gong for Mosman</li><li>Jenna Hollis wins the Australian Women's AC Open 2018 Eire Cup, Adelaide</li></ul>
        <a class="read-more" href="#">Read more</a>
      </article>
    </div>
  </div>
</section>

<section class="officials">
  <div class="container">
    <h2 class="section-title">OFFICIALS &amp; VOLUNTEERS</h2>
    <div class="gallery">
      <div class="tile tile-play" role="img" aria-label="Two players on a croquet lawn with houses behind"></div>
      <div class="tile tile-support">
        <h5>TEAM SUPPORT</h5>
        <p>Lorem Ipsum is simply dummy text of the printing and typesetting industry.</p>
      </div>
      <div class="tile tile-gear" role="img" aria-label="Croquet mallets, balls and a rule book on the ground"></div>
      <div class="tile tile-night" role="img" aria-label="Croquet balls and a hoop on a lawn at night under lights"></div>
    </div>
  </div>
</section>

<footer class="site-footer">
  <div class="footer-col" style="left:186px">
    <h6>CONTACT</h6>
    <p class="footer-label" style="margin-left:1px">LOCATION</p>
    <p class="footer-text">Pellmark Sporting League Inc.<br>Harlow Park<br>Fenwick NSW 2199</p>
    <p class="footer-label" style="margin-top:16px">TELEPHONE</p>
    <p class="footer-text">(02) 9000 4821</p>
    <p class="footer-label" style="margin-top:24px">EMAIL</p>
    <p class="footer-text">hello@pellmark-league.org</p>
  </div>
  <div class="footer-col" style="left:490px">
    <h6>LINKS</h6>
    <ul class="footer-links" style="width:65px">
      <li><a href="#">Home</a></li><li><a href="#">About</a></li><li><a href="#">Join Club</a></li><li><a href="#">Events</a></li><li><a href="#">Newsletters</a></li><li><a href="#">Officials</a></li><li><a href="#">Sitemap</a></li>
    </ul>
  </div>
  <div class="footer-col" style="left:714px">
    <h6>NEWSLETTER</h6>
    <p class="footer-label" style="font-weight:600">Subscribe our newsletter</p>
    <form class="subscribe"><input type="text" placeholder="ENTER YOUR EMAIL"><button type="button">SEND</button></form>
    <p class="footer-label" style="margin-top:14px">FOLLOW US</p>
    <div class="social">
      <span aria-label="Social link"></span>
      <span aria-label="Social link"></span>
      <span aria-label="Social link"></span>
      <span aria-label="Email"><svg width="20" height="16" viewBox="0 0 20 16"><rect width="20" height="16" rx="2" fill="#fff"/><path d="m1 2 9 7 9-7" fill="none" stroke="#5a5a5a" stroke-width="1.6"/></svg></span>
    </div>
  </div>
  <div class="copyright">Copyright&nbsp;
    <svg width="14" height="14" viewBox="0 0 14 14" fill="none" stroke="#fff" stroke-width="1.2"><circle cx="7" cy="7" r="6"/><path d="M9 5.2a2.6 2.6 0 1 0 0 3.6"/></svg>
    &nbsp;Pellmark Sporting League. All rights reserved.</div>
</footer>

</body>
</html>
```